Glow Ridge inc New website
tanning salon
Thanks so much! We really like #18 and 19.
We like the colors on #15 and #13 too.
Like #12 and #14 - can the beds at the bottom be a scroll bar with lots of different bed pictures?
The images so far are not really our image. We have more hip yet conservative customer base. Any pics with men & women? Does not have to be on beach. Not using our old saying "we didn't invent tanning.... Please keep submitting!!
Like #2 better but not sure about the yellow up in the header by our logo.
Thanks.
Can you change the background to more of a yellow instead of brownish yellow?
Thanks!
I uploaded our logo.

```html
<!DOCTYPE html>
<html lang="en">
<head>
<meta charset="utf-8">
<title>Glow Ridge inc</title>
<link rel="stylesheet" href="https://fonts.googleapis.com/css2?family=Arimo:wght@400;700&family=Handlee&display=swap">
<style>
:root{
  --sky-top:#5aa6d8;
  --sky-mid:#d9c59a;
  --sky-low:#f2b23a;
  --sky-deep:#e58a1c;
  --top-band:#2f8fe0;
  --nav:#1f7fd0;
  --nav-dark:#1566b0;
  --nav-text:#ffffff;
  --hero-a:#8fd0f2;
  --hero-b:#d9f1fb;
  --hero-title:#1b8fd6;
  --hero-sub:#ffffff;
  --logo:#1a2a3a;
  --logo-sun:#f6b81c;
  --panel:rgba(250,236,200,0.72);
  --rule:rgba(160,130,80,0.35);
  --heading:#2a2a2a;
  --body:#5a5040;
  --more:#222222;
  --footer:#111111;
  --footer-text:#d8d8d8;
}
*{box-sizing:border-box;margin:0;padding:0}
html,body{width:1200px;height:854px;overflow:hidden}
body{font-family:"Arimo",Arial,sans-serif;position:relative}
.backdrop{position:absolute;inset:0;background:linear-gradient(180deg,var(--sky-top) 0%,#9bbfd6 25%,var(--sky-mid) 50%,var(--sky-low) 78%,var(--sky-deep) 100%)}
.top-band{position:absolute;left:0;top:0;width:1200px;height:34px;background:var(--top-band)}
.site{position:absolute;left:173px;top:34px;width:859px}
.header{display:flex;height:273px}
.brand{width:295px;background:#fff;display:flex;align-items:center;justify-content:center;gap:10px}
.brand-mark{width:30px;height:30px;border-radius:50%;background:var(--logo-sun)}
.brand-name{font-weight:700;font-size:30px;color:var(--logo)}
.hero{flex:1;position:relative;background:linear-gradient(160deg,var(--hero-b) 0%,var(--hero-a) 60%,#4fb0e6 100%)}
.hero-text{position:absolute;left:22px;top:28px}
.hero-kicker{font-family:"Handlee",cursive;font-size:25px;color:#fff;text-shadow:0 1px 2px rgba(0,0,0,.25)}
.hero-title{font-family:"Handlee",cursive;font-size:46px;color:var(--hero-title);margin:4px 0 0 4px}
.hero-sub{font-size:15px;color:var(--hero-sub);margin-top:6px}
.nav{height:41px;background:linear-gradient(180deg,var(--nav) 0%,var(--nav-dark) 100%);display:flex;align-items:center;justify-content:center;gap:18px;color:var(--nav-text);font-size:14px;list-style:none}
.nav li+li::before{content:"|";margin-right:18px}
.content{margin-top:12px;height:413px;background:var(--panel);position:relative}
.col-divider{position:absolute;left:552px;top:24px;width:1px;height:370px;background:var(--rule)}
.row-divider{position:absolute;left:22px;top:204px;width:815px;height:1px;background:var(--rule)}
h2{font-weight:400;font-size:18px;color:var(--heading)}
p{font-size:11.5px;line-height:18px;color:var(--body)}
.more{font-size:12px;color:var(--more);text-align:right;margin-top:2px}
.news{position:absolute;left:22px;top:28px;width:520px}
.news-body{display:flex;gap:12px;margin-top:-6px}
.news-photo{width:223px;height:113px;background:linear-gradient(135deg,#9fd4ee,#e9d3b8 55%,#6fb3dc);flex:none;margin-top:12px}
.products{position:absolute;left:572px;top:28px;width:260px}
.products-photo{width:216px;height:108px;margin-top:4px;background:linear-gradient(90deg,#fff,#e9c895 40%,#b5753c 70%,#f5efe3)}
.equipment{position:absolute;left:27px;top:240px;width:515px}
.follow{position:absolute;left:572px;top:255px}
.social{display:flex;gap:14px;margin-top:14px}
.social span{width:50px;height:50px;border:1px solid #c9b48a;background:#f6ead0;display:flex;align-items:center;justify-content:center}
.social span::after{content:"";width:34px;height:34px;border-radius:6px;background:var(--c)}
.footer{margin-top:5px;height:24px;background:var(--footer);color:var(--footer-text);font-size:12px;text-align:right;padding:5px 12px}
</style>
</head>
<body>
<div class="backdrop" role="img" aria-label="Sunset sky with clouds over a golden horizon"></div>
<div class="top-band"></div>
<div class="site">
  <header class="header">
    <div class="brand"><span class="brand-mark"></span><span class="brand-name">Glow Ridge inc</span></div>
    <div class="hero" role="img" aria-label="Woman in a bikini relaxing in bright blue water">
      <div class="hero-text">
        <div class="hero-kicker">Sometimes, You Just Need to</div>
        <div class="hero-title">Whiten Up</div>
        <div class="hero-sub">The Part of Your Body that's Better White!</div>
      </div>
    </div>
  </header>
  <ul class="nav">
    <li>Home</li><li>About us</li><li>Tanning Equipment</li><li>Tanning Lotions</li><li>Services</li><li>Daily Specials</li><li>Contact us</li>
  </ul>
  <main class="content">
    <div class="col-divider"></div>
    <div class="row-divider"></div>
    <section class="news">
      <h2>News</h2>
      <div class="news-body">
        <div class="news-photo" role="img" aria-label="Woman lying in shallow surf on a beach"></div>
        <div>
          <p>Calder Hall is An Institution With A Difference. A walk along the corridor is an education in itself. Well equipped science labs, a library with a good collection of study materials and reference books, a tastefully designed seminar Hall &amp; Media Research Center are a Boone in itself.</p>
          <div class="more">More....</div>
        </div>
      </div>
    </section>
    <section class="products">
      <h2>Our Products</h2>
      <div class="products-photo" role="img" aria-label="Row of tanning lotion bottles and tubes"></div>
    </section>
    <section class="equipment">
      <h2>Tanning Equipment</h2>
      <p>Calder Hall is An Institution With A Difference. A walk along the corridor is an education in itself. Well equipped science labs, a library with a good collection of study materials and reference books, a tastefully designed seminar Hall &amp; Media Research Center are a Boone in itself. Well equipped science labs, a library with a good collection of study materials and reference books, a tastefully designed seminar Hall &amp; Media Research Center are a Boone in itself.</p>
      <div class="more">More....</div>
    </section>
    <section class="follow">
      <h2>Follow us on</h2>
      <div class="social">
        <span style="--c:#3b5a9a" aria-label="Social network link"></span>
        <span style="--c:#4ab3e6" aria-label="Social network link"></span>
        <span style="--c:#c8282a" aria-label="Video channel link"></span>
      </div>
    </section>
  </main>
  <footer class="footer">Copyright@glowridgeinc</footer>
</div>
</body>
</html>
```